Borlavex Management

We need a web design for a new consulting company, with clients all over the world. The company provides management consulting to the travel industry.

Logo files are attached.

Website must look very corporate and be responsive in design.

Management Consulting

```html
<!DOCTYPE html>
<html lang="en">
<head>
<meta charset="utf-8">
<title>Borlavex Management</title>
<link rel="stylesheet" href="https://fonts.googleapis.com/css2?family=Titillium+Web:wght@400;600;700&family=Open+Sans:wght@400;600;700&family=Tinos&display=swap">
<style>
:root{
  --brand-blue:#1e73be;
  --brand-blue-dark:#0b5aa0;
  --accent-red:#d42a1e;
  --ink:#222;
  --ink-soft:#555;
  --white:#fff;
  --card-bg:#e6e6e6;
  --strip-dark:#1f1f1f;
  --footer:#3e4347;
  --footer-bottom:#33373a;
  --footer-text:#c9cdd0;
  --rule:#5a5f63;
}
*{box-sizing:border-box;margin:0;padding:0}
html,body{width:1200px;height:2528px;overflow:hidden;background:var(--white)}
body{position:relative;font-family:"Open Sans",Arial,sans-serif;color:var(--ink)}
.abs{position:absolute}
.top-rule{left:0;top:0;width:1200px;height:8px;background:var(--brand-blue)}
.header{left:0;top:8px;width:1200px;height:110px;background:var(--white)}
.brand{left:98px;top:38px;display:flex;align-items:center;gap:14px}
.brand-mark{width:50px;height:50px;border-radius:50%;background:var(--brand-blue)}
.brand-name{font-family:"Titillium Web",sans-serif;font-weight:700;font-size:30px;color:var(--brand-blue-dark);letter-spacing:.5px}
.nav{left:593px;top:41px;display:flex;align-items:center;gap:0}
.nav a{font-family:"Titillium Web",sans-serif;font-size:16px;color:var(--ink);text-decoration:none;height:34px;line-height:34px;padding:0 16px;margin-right:10px}
.nav a.is-active{background:var(--brand-blue);color:var(--white);border-radius:3px}
.hero{left:0;top:118px;width:1200px;height:536px;background:linear-gradient(120deg,#c9d5e0 0%,#e9eef3 35%,#b9c6d2 65%,#8d9bab 100%)}
.hero-arrow{top:340px;width:30px;height:36px}
.hero-dots{left:572px;top:620px;display:flex;gap:5px}
.hero-dots span{width:9px;height:9px;border-radius:50%;border:1.5px solid #555;background:var(--white)}
.hero-dots span.on{background:#2db34a;border-color:#2db34a}
.welcome{left:0;top:668px;width:1200px;text-align:center}
.welcome h1{font-family:"Titillium Web",sans-serif;font-weight:600;font-size:30px;color:var(--brand-blue)}
.welcome p{width:1000px;margin:12px auto 0;font-size:11.5px;line-height:21px;font-weight:600;color:#444}
.services{left:0;top:844px;width:1200px;height:359px;background:linear-gradient(160deg,#3a332d 0%,#2a2521 50%,#43392f 100%)}
.section-title-light{font-family:"Titillium Web",sans-serif;font-weight:600;font-size:28px;color:var(--white);text-align:center}
.service{width:330px;text-align:center;color:var(--white)}
.service-icon{width:80px;height:80px;margin:0 auto;border-radius:50%;background:var(--white);display:flex;align-items:center;justify-content:center}
.service-icon i{display:flex;width:66px;height:66px;border-radius:50%;background:var(--brand-blue);align-items:center;justify-content:center}
.service h3{font-family:"Titillium Web",sans-serif;font-weight:600;font-size:23px;margin-top:26px}
.service p{font-size:12px;line-height:21px;margin-top:10px;padding:0 40px}
.read-more{font-size:12px;color:var(--accent-red);margin-top:10px;display:block}
.news-head{left:0;top:1236px;width:1200px;text-align:center}
.news-head h2{font-family:"Titillium Web",sans-serif;font-weight:600;font-size:28px;color:var(--brand-blue)}
.news-head p{font-size:14px;margin-top:10px;color:var(--ink)}
.news-card{top:1343px;width:311px;height:317px;background:var(--card-bg);border-top:4px solid var(--brand-blue);box-shadow:0 14px 16px -10px rgba(0,0,0,.35)}
.news-photo{height:181px;position:relative}
.news-date{position:absolute;right:0;top:0;width:57px;height:59px;background:var(--brand-blue);color:var(--white);text-align:center;font-family:"Titillium Web",sans-serif;font-size:13px;line-height:18px;padding-top:6px}
.news-date b{display:block;font-size:21px;font-weight:600;line-height:24px}
.news-body{padding:8px 8px}
.news-body h4{font-size:14px;font-weight:700;color:var(--ink)}
.news-body p{font-size:11px;line-height:18px;color:#666;margin-top:6px}
.news-body .read-more{font-size:11px;margin-top:4px}
.testimonials{left:0;top:1709px;width:1200px;height:301px;background:linear-gradient(100deg,#5a4a3a 0%,#8a7a5e 40%,#6f5e48 70%,#3f3328 100%)}
.avatar{left:125px;top:1809px;width:134px;height:134px;border-radius:50%;border:4px solid var(--white);background:linear-gradient(180deg,#d6dbe0,#8a96a3)}
.quote{left:285px;top:1845px;width:800px;font-family:"Tinos",Georgia,serif;font-size:19px;line-height:30px;color:var(--white)}
.quote-author{left:900px;top:1950px;width:180px;text-align:right;font-family:"Tinos",Georgia,serif;font-size:18px;color:var(--white)}
.partners{left:0;top:2010px;width:1200px;height:125px;display:flex;justify-content:center;align-items:center;gap:60px}
.partner-badge{width:150px;height:36px;border-radius:4px;background:#d9dde2}
.contact-strip{left:0;top:2135px;width:1200px;height:120px;background:var(--strip-dark)}
.contact-item{top:2158px;width:200px;text-align:center;color:var(--white)}
.contact-item span{display:block;font-size:17px;margin-top:12px}
.footer{left:0;top:2255px;width:1200px;height:208px;background:var(--footer);color:var(--footer-text)}
.footer-col{top:2283px;font-size:11px;line-height:17px}
.footer-col h5{font-size:12.5px;font-weight:700;color:var(--white);letter-spacing:.3px;margin-bottom:14px}
.footer-col b{color:var(--white);font-weight:600}
.contact-line{display:flex;gap:10px;margin-bottom:8px;width:240px}
.contact-line svg{flex:none;margin-top:3px}
.post{width:240px;border-bottom:1px solid var(--rule);padding-bottom:10px;margin-bottom:12px}
.post b{display:block}
.newsletter-form{display:flex;margin-top:24px}
.newsletter-form .field{width:161px;height:28px;background:#f3f3f3}
.newsletter-form .submit{width:63px;height:28px;background:#0a86c9;color:var(--white);font-size:10.5px;font-weight:700;display:flex;align-items:center;justify-content:center}
.social{display:flex;gap:7px}
.social span{width:26px;height:26px;border-radius:50%;background:#f2f2f2}
.lang{margin-top:36px;margin-left:94px;width:66px;height:28px;background:#f3f3f3;display:flex;align-items:center;padding-left:8px;gap:14px}
.lang i{width:22px;height:14px;background:#2f4f8f}
.footer-bottom{left:0;top:2463px;width:1200px;height:65px;background:var(--footer-bottom);color:var(--footer-text);font-size:11px}
.footer-bottom .copy{position:absolute;left:99px;top:24px}
.footer-bottom .links{position:absolute;right:100px;top:24px;display:flex;gap:22px}
</style>
</head>
<body>
<div class="abs top-rule"></div>

<header class="abs header">
  <div class="abs brand" style="top:30px">
    <span class="brand-mark"></span>
    <span class="brand-name">Borlavex Management</span>
  </div>
  <nav class="abs nav">
    <a class="is-active">Home</a><a>About Us</a><a>Services</a><a>Blog</a><a>Contact Us</a>
  </nav>
</header>

<section class="abs hero" role="img" aria-label="Photo of four consultants in a meeting at a bright office table"></section>
<svg class="abs hero-arrow" style="left:54px" viewBox="0 0 30 36"><path d="M22 3 L8 18 L22 33" fill="none" stroke="#fff" stroke-width="5"/></svg>
<svg class="abs hero-arrow" style="left:1128px" viewBox="0 0 30 36"><path d="M8 3 L22 18 L8 33" fill="none" stroke="#fff" stroke-width="5"/></svg>
<div class="abs hero-dots"><span class="on"></span><span></span><span></span></div>

<section class="abs welcome">
  <h1>Welcome To Borlavex</h1>
  <p>Lorem ipsum dolor sit amet, consectetuer adipiscing elit, sed diam nonummy nibh euismod tincidunt ut laoreet dolore magna aliquam erat volutpat. Ut wisi enim ad minim veniam, quis nostrud exerci tation ullamcorper suscipit lobortis nisl ut aliquip ex ea commodo consequat. Lorem ipsum dolor sit amet, consectetuer adipiscing elit, sed diam nonummy nibh euismod tincidunt ut laoreet dolore magna aliquam erat volutpat. Ut wisi enim ad minim veniam, quis nostrud exerci tation ullamcorper suscipit lobortis nisl ut aliquip ex ea commodo consequat.</p>
</section>

<section class="abs services" role="img" aria-label="Dark background photo of a desk with a laptop">
  <h2 class="abs section-title-light" style="left:0;top:22px;width:1200px">Services</h2>
  <div class="abs service" style="left:71px;top:88px">
    <div class="service-icon"><i><svg width="30" height="30" viewBox="0 0 30 30"><path d="M15 3 C24 10 24 22 15 27 C6 22 6 10 15 3Z" fill="#fff"/><path d="M15 8 V25" stroke="#1e73be" stroke-width="2"/></svg></i></div>
    <h3>Post Your Idea</h3>
    <p>This template was designed specially for you. It's easy to customize anything. Fully responsive layout to customize anything. Fully responsive layout</p>
    <span class="read-more">Read More »</span>
  </div>
  <div class="abs service" style="left:433px;top:88px">
    <div class="service-icon"><i><svg width="30" height="34" viewBox="0 0 30 34"><circle cx="15" cy="13" r="10" fill="#fff"/><rect x="10" y="23" width="10" height="7" fill="#fff"/><text x="15" y="18" font-size="13" font-family="Open Sans,sans-serif" font-weight="700" text-anchor="middle" fill="#1e73be">$</text></svg></i></div>
    <h3>Get Investor</h3>
    <p>This template was designed specially for you. It's easy to customize anything. Fully responsive layout to customize anything. Fully responsive layout</p>
    <span class="read-more">Read More »</span>
  </div>
  <div class="abs service" style="left:779px;top:88px">
    <div class="service-icon"><i><svg width="36" height="30" viewBox="0 0 36 30"><path d="M18 3 L28 18 H8 Z" fill="#fff"/><path d="M3 21 H33 L29 27 H7 Z" fill="#fff"/></svg></i></div>
    <h3>Start Business</h3>
    <p>This template was designed specially for you. It's easy to customize anything. Fully responsive layout to customize anything. Fully responsive layout</p>
    <span class="read-more">Read More »</span>
  </div>
</section>

<section class="abs news-head">
  <h2>Latest News</h2>
  <p>Lorem ipsum dolor sit amet, consectetuer adipiscing elit, sed diam</p>
</section>

<article class="abs news-card" style="left:99px">
  <div class="news-photo" role="img" aria-label="Photo of a businesswoman beside a digital globe" style="background:linear-gradient(135deg,#f2f4f6,#c5ccd4)"><div class="news-date">Sun<b>12</b></div></div>
  <div class="news-body"><h4>Lorem ipsum</h4><p>Lorem ipsum dolor sit amet, consectetuer adipiscing elit, sed diam nonummy nibh euismod tincidunt ut laoreet dolore magna aliquam erat volutpat.</p><span class="read-more">Read More...</span></div>
</article>
<article class="abs news-card" style="left:441px">
  <div class="news-photo" role="img" aria-label="Photo of a hand touching a tablet with glowing data" style="background:linear-gradient(135deg,#9fc3e6,#2f5f94)"><div class="news-date">Sun<b>12</b></div></div>
  <div class="news-body"><h4>Lorem ipsum</h4><p>Lorem ipsum dolor sit amet, consectetuer adipiscing elit, sed diam nonummy nibh euismod tincidunt ut laoreet dolore magna aliquam erat volutpat.</p><span class="read-more">Read More...</span></div>
</article>
<article class="abs news-card" style="left:788px">
  <div class="news-photo" role="img" aria-label="Photo of a business team gathered around a laptop" style="background:linear-gradient(135deg,#eceeef,#6b6f75)"><div class="news-date">Sun<b>12</b></div></div>
  <div class="news-body"><h4>Lorem ipsum</h4><p>Lorem ipsum dolor sit amet, consectetuer adipiscing elit, sed diam nonummy nibh euismod tincidunt ut laoreet dolore magna aliquam erat volutpat.</p><span class="read-more">Read More...</span></div>
</article>

<section class="abs testimonials" role="img" aria-label="Blurred photo of a hiker in a mountain landscape">
  <h2 class="abs section-title-light" style="left:0;top:38px;width:1200px">Testimonials</h2>
</section>
<div class="abs avatar" role="img" aria-label="Portrait of the client"></div>
<p class="abs quote">As soon as I saw this theme it was love at first site, I knew I had to somehow get it to notice me, !so I did what any good man would do... I used money to buy its affections</p>
<p class="abs quote-author">— Darel Onwick</p>

<section class="abs partners">
  <span class="partner-badge"></span><span class="partner-badge"></span><span class="partner-badge"></span><span class="partner-badge"></span><span class="partner-badge"></span>
</section>

<section class="abs contact-strip"></section>
<div class="abs contact-item" style="left:42px">
  <svg width="26" height="26" viewBox="0 0 24 24"><path d="M6 2 L10 6 L8 9 C9 12 12 15 15 16 L18 14 L22 18 L19 22 C10 21 3 14 2 5 Z" fill="#fff"/></svg>
  <span>Talk to u</span>
</div>
<div class="abs contact-item" style="left:333px">
  <svg width="30" height="26" viewBox="0 0 30 26"><ellipse cx="15" cy="11" rx="13" ry="9" fill="#fff"/><path d="M6 17 L4 24 L12 19Z" fill="#fff"/></svg>
  <span>Live Chat</span>
</div>
<div class="abs contact-item" style="left:626px">
  <svg width="30" height="24" viewBox="0 0 30 24"><rect x="1" y="2" width="28" height="20" rx="2" fill="#fff"/><path d="M2 4 L15 14 L28 4" fill="none" stroke="#1f1f1f" stroke-width="2"/></svg>
  <span>Email Us</span>
</div>
<div class="abs contact-item" style="left:918px">
  <svg width="28" height="26" viewBox="0 0 28 26"><rect x="1" y="11" width="6" height="14" fill="#fff"/><path d="M9 11 L15 2 C18 2 18 5 17 9 H25 C27 9 27 12 26 13 L23 24 H9 Z" fill="#fff"/></svg>
  <span>Good Support</span>
</div>

<footer class="abs footer"></footer>
<div class="abs footer-col" style="left:99px">
  <h5>CONTACT INFO</h5>
  <div class="contact-line"><svg width="8" height="11" viewBox="0 0 8 11"><path d="M4 0 C7 0 8 2 8 4 C8 6 4 11 4 11 C4 11 0 6 0 4 C0 2 1 0 4 0Z" fill="#8a9095"/></svg><div><b>Address:</b> 4120 Harlow Street, 60210 Linden, Austria</div></div>
  <div class="contact-line"><svg width="8" height="11" viewBox="0 0 8 11"><rect x="1" y="0" width="6" height="11" rx="1" fill="#8a9095"/></svg><div><b>Telephones:</b> +1 555 014-2237</div></div>
  <div class="contact-line"><svg width="10" height="8" viewBox="0 0 10 8"><rect width="10" height="8" fill="#8a9095"/></svg><div><b>E-mail:</b> contacts@borlavex.com</div></div>
</div>
<div class="abs footer-col" style="left:379px">
  <h5>RECENT POSTS</h5>
  <div class="post"><b>This is a Standard Post</b>November 21, 2013</div>
  <div class="post"><b>This is a Gallery Post</b>October 20, 2013</div>
</div>
<div class="abs footer-col" style="left:659px">
  <h5>NEWSLETTER</h5>
  <p style="width:250px">Subscribe and stay up to date with the latest news from us.</p>
  <div class="newsletter-form"><span class="field"></span><span class="submit">SUBMIT</span></div>
</div>
<div class="abs footer-col" style="left:939px">
  <h5>FOLLOW US</h5>
  <div class="social"><span></span><span></span><span></span><span></span><span></span></div>
  <div class="lang"><i></i><svg width="8" height="5" viewBox="0 0 8 5"><path d="M0 0 H8 L4 5Z" fill="#555"/></svg></div>
</div>

<div class="abs footer-bottom">
  <span class="copy">Content copyright 2014. Borlavex. All rights reserved.</span>
  <span class="links"><span>FAQ's</span><span>About</span><span>Contact</span></span>
</div>
</body>
</html>
```